Creative Workshop Business needs a Promotional flyer

We need a promotional brochure for our business. We will provide you with the copy to include in the brochure. The look were are trying to achieve is clean, less is more and provide crisp visuals to communicate our message. We would like you to think outside the box in your design but remember we are a kids creative craft and art workshop business - so fun but not too kiddie! We have attached our logo, images to use and examples (marked examples #1 etc) that we love. Once this brochure has been created we would like to continue to work with the designer to create our marketing suite for our business. We have attached a lo res design of our trailer signage as an example and maybe a place to start designing.
When using the logo please not that the wording "CREATIVE WORKSHOPS IS REPLACED WITH CREATIVE WORKSHOPS FOR KIDS".
We have attached our font as well but are happy for suggestions on font.
If there is any clarification needed please contact tara@pebblehollowarts.com.au

• Font has been provided

• Great visuals and use the images provided.
• Easy to read and follow but more than your usually tri-fold design. We want customers to pick up our flyer above anyone else'.

```html
<!DOCTYPE html>
<html lang="en">
<head>
<meta charset="utf-8">
<title>Pebble Hollow Arts – Creative Workshops for Kids</title>
<link rel="stylesheet" href="https://fonts.googleapis.com/css2?family=Oswald:wght@400;500&family=Josefin+Sans:wght@300;400&display=swap">
<style>
  :root {
    --brand-blue: #175ea1;
    --accent-pink: #d2185e;
    --ink: #111111;
    --paper: #ffffff;
  }
  html, body {
    margin: 0;
    padding: 0;
    width: 1200px;
    height: 1200px;
    overflow: hidden;
    background: var(--brand-blue);
  }
  .flyer {
    position: relative;
    width: 1200px;
    height: 1200px;
    overflow: hidden;
  }
  .flyer-art {
    position: absolute;
    inset: 0;
  }
  .franchise-badge {
    position: absolute;
    left: 572px;
    top: 130px;
    width: 300px;
    text-align: center;
    font-family: "Oswald", sans-serif;
    white-space: nowrap;
  }
  .franchise-badge__headline {
    margin: 0;
    color: var(--accent-pink);
    font-weight: 400;
    font-size: 32px;
    line-height: 35px;
    text-transform: uppercase;
    letter-spacing: -0.5px;
  }
  .franchise-badge__phone {
    display: inline-block;
    margin: 0;
    color: var(--ink);
    font-weight: 500;
    font-size: 62px;
    line-height: 72px;
    letter-spacing: -2px;
    transform: scaleX(0.88);
    transform-origin: center;
  }
  .franchise-badge__email {
    margin: 4px 0 0;
    color: var(--ink);
    font-weight: 400;
    font-size: 18px;
    line-height: 24px;
    letter-spacing: -0.2px;
  }
  .brand-info {
    position: absolute;
    left: 208px;
    top: 544px;
    width: 400px;
    text-align: center;
    color: var(--paper);
    font-family: "Josefin Sans", sans-serif;
    font-weight: 300;
  }
  .brand-info__tagline {
    margin: 0 0 34px;
    font-size: 21px;
    letter-spacing: 0.5px;
    text-transform: uppercase;
  }
  .brand-info__line {
    margin: 0;
    color: var(--paper);
    font-size: 13px;
    line-height: 28px;
    letter-spacing: 4px;
    text-transform: uppercase;
  }
  .brand-info__line--phone {
    font-size: 20px;
    letter-spacing: 4px;
    font-weight: 300;
  }
  .social-list {
    position: absolute;
    left: 64px;
    top: 777px;
    margin: 0;
    padding: 0;
    list-style: none;
    color: var(--paper);
    font-family: "Josefin Sans", sans-serif;
    font-weight: 400;
    font-size: 13px;
    letter-spacing: 0.3px;
  }
  .social-list__item {
    display: flex;
    align-items: center;
    height: 32px;
    margin-bottom: 42px;
  }
  .social-list__dot {
    width: 30px;
    height: 30px;
    border: 1.5px solid var(--paper);
    border-radius: 50%;
    margin-right: 30px;
    box-sizing: border-box;
  }
</style>
</head>
<body>
<main class="flyer">
  <svg class="flyer-art" width="1200" height="1200" viewBox="0 0 1200 1200">
    <defs>
      <linearGradient id="paintingGrad" x1="0" y1="0" x2="1" y2="1">
        <stop offset="0" stop-color="#d9e6ee"/>
        <stop offset="0.5" stop-color="#8fb4d4"/>
        <stop offset="1" stop-color="#e9d98a"/>
      </linearGradient>
      <linearGradient id="studioGrad" x1="0" y1="0" x2="1" y2="1">
        <stop offset="0" stop-color="#f0eeec"/>
        <stop offset="0.55" stop-color="#8a7a70"/>
        <stop offset="1" stop-color="#2c2a2c"/>
      </linearGradient>
      <linearGradient id="groupGrad" x1="0" y1="0" x2="1" y2="1">
        <stop offset="0" stop-color="#e7e4e2"/>
        <stop offset="0.6" stop-color="#9ab2c9"/>
        <stop offset="1" stop-color="#3c5d86"/>
      </linearGradient>
    </defs>

    <rect class="flyer-bg" width="1200" height="1200" fill="var(--brand-blue)"/>

    <path class="photo photo--painting" role="img" aria-label="Photo: a girl in a yellow top beside a colourful painted mural"
          d="M0 0 H441 A560 560 0 0 1 0 546 Z" fill="url(#paintingGrad)"/>

    <circle class="photo photo--group" role="img" aria-label="Photo: a smiling girl making a craft piece with other children in a bright studio"
            cx="644" cy="1241" r="473" fill="url(#groupGrad)"/>

    <circle class="photo photo--maker" role="img" aria-label="Photo: a smiling girl in a patterned dress working on a craft activity"
            cx="1099" cy="707" r="459" fill="url(#studioGrad)"/>

    <g class="badge-ring" fill="none" stroke="var(--accent-pink)">
      <circle cx="722" cy="259" r="202" stroke-width="1.6" stroke-dasharray="6 5"/>
      <path d="M600 98 A202 202 0 0 1 718 57" stroke-width="5.5"/>
      <path d="M823 84 A202 202 0 0 1 860 407" stroke-width="5.5"/>
      <path d="M595 416 A202 202 0 0 1 547 158" stroke-width="5.5"/>
    </g>
    <circle class="badge-disc" cx="722" cy="259" r="165" fill="var(--paper)"/>
  </svg>

  <section class="franchise-badge">
    <h1 class="franchise-badge__headline">Business<br>Opportunities<br>Available</h1>
    <p class="franchise-badge__phone">1300 482 617</p>
    <p class="franchise-badge__email">franchise@pebblehollowarts.com.au</p>
  </section>

  <section class="brand-info">
    <p class="brand-info__tagline">Creative Workshops for Kids</p>
    <p class="brand-info__line">www.pebblehollowarts.com.au</p>
    <p class="brand-info__line brand-info__line--phone">1300 482 617</p>
    <p class="brand-info__line">hello@pebblehollowarts.com.au</p>
  </section>

  <ul class="social-list">
    <li class="social-list__item"><span class="social-list__dot"></span>/PEBBLEHOLLOWARTS</li>
    <li class="social-list__item"><span class="social-list__dot"></span>@PEBBLEHOLLOWARTS</li>
  </ul>
</main>
</body>
</html>
```